Letter Head

We need a letter head desgn (A4).
Header Marcus Pellow Creative
phone number 0438705164
email marcuspellowcreative@fernmail.example

Footer ABN 37 512 640 915

```html
<!DOCTYPE html>
<html lang="en">
<head>
<meta charset="utf-8">
<title>Marcus Pellow Creative – Letterhead</title>
<link rel="stylesheet" href="https://fonts.googleapis.com/css2?family=Arimo:wght@400;700&display=swap">
<style>
  :root {
    --lime: #a3d117;
    --lime-soft: #bfe07f;
    --page: #edf5e3;
    --facet-pale: #f6f9ec;
    --facet-mint: #e1f1e6;
    --facet-sage: #e6f2dc;
    --facet-sea: #dcefe2;
    --ink-dark: #1b1b1d;
    --ink-indigo: #303152;
    --ink-teal: #1f6668;
    --white: #ffffff;
    --placeholder: #f8fbf3;
  }
  * { box-sizing: border-box; margin: 0; padding: 0; }
  html, body { width: 900px; height: 1200px; overflow: hidden; background: var(--white); }
  body { font-family: "Arimo", Arial, sans-serif; }

  .letterhead { position: relative; width: 900px; height: 1200px; overflow: hidden; background: var(--page); }
  .letterhead__backdrop { position: absolute; inset: 0; width: 900px; height: 1200px; }

  .brand { position: absolute; left: 50px; top: 50px; display: flex; align-items: flex-start; gap: 16px; }
  .brand__name {
    color: var(--white); font-weight: 700; font-size: 46px; line-height: 46px;
    text-transform: uppercase; letter-spacing: -0.5px;
  }
  .brand__services {
    color: var(--white); font-weight: 400; font-size: 15px; line-height: 15px; padding-top: 6px;
    list-style: none;
  }

  .hero-mark {
    position: absolute; left: 271px; top: 472px; width: 358px; height: 254px;
    background: var(--placeholder); opacity: 0.85;
  }

  .footer-contacts {
    position: absolute; left: 50px; top: 1106px; list-style: none;
    color: var(--white); font-size: 13px; line-height: 22px;
  }
  .footer-contacts li { display: flex; align-items: center; gap: 6px; }
  .footer-contacts svg { width: 11px; height: 11px; flex: none; }

  .abn {
    position: absolute; left: 650px; top: 1112px;
    color: var(--white); font-size: 20px; line-height: 24px;
  }
</style>
</head>
<body>
<main class="letterhead">
  <svg class="letterhead__backdrop" viewBox="0 0 900 1200" aria-hidden="true">
    <defs>
      <linearGradient id="headerGlow" x1="0" y1="0" x2="1" y2="0.4">
        <stop offset="0" stop-color="#9ed36a"/>
        <stop offset="1" stop-color="#c6e58a"/>
      </linearGradient>
      <linearGradient id="footerBand" x1="0" y1="0" x2="1" y2="0">
        <stop offset="0" stop-color="#1b1b1d"/>
        <stop offset="0.4" stop-color="#222226"/>
        <stop offset="0.7" stop-color="#303152"/>
        <stop offset="1" stop-color="#1f6668"/>
      </linearGradient>
    </defs>

    <!-- body facets -->
    <rect class="facet" x="0" y="182" width="900" height="906" fill="var(--page)"/>
    <polygon points="0,182 900,182 900,310 560,470 0,250" fill="var(--facet-pale)"/>
    <polygon points="560,470 900,310 900,330 0,760 0,250" fill="#eff6e4"/>
    <polygon points="900,330 900,1088 700,1088 500,950" fill="var(--facet-mint)"/>
    <polygon points="0,760 500,950 420,1088 0,1088" fill="var(--facet-sea)"/>
    <polygon points="500,950 700,1088 420,1088" fill="var(--facet-sage)"/>

    <!-- header band -->
    <rect x="0" y="0" width="900" height="184" fill="var(--lime)"/>
    <polygon points="0,20 580,184 0,184" fill="url(#headerGlow)"/>

    <!-- footer band -->
    <rect x="0" y="1088" width="900" height="112" fill="url(#footerBand)"/>
    <polygon points="240,1200 420,1100 600,1200" fill="#26263a" opacity="0.7"/>
  </svg>

  <header class="brand">
    <h1 class="brand__name">Marcus Pellow<br>Creative</h1>
    <ul class="brand__services">
      <li>photography</li>
      <li>video</li>
      <li>design</li>
    </ul>
  </header>

  <div class="hero-mark" role="img" aria-label="Large pale video camera icon as a watermark motif"></div>

  <footer>
    <ul class="footer-contacts">
      <li>
        <svg viewBox="0 0 12 12" aria-hidden="true"><circle cx="6" cy="6" r="6" fill="#fff"/><path d="M3.5 3.2l1.3-.4.8 1.7-.8.6c.4.9 1 1.5 1.9 1.9l.6-.8 1.7.8-.4 1.3c-3 0-5.1-2.1-5.1-5.1z" fill="#1b1b1d"/></svg>
        0438.705.164
      </li>
      <li>
        <svg viewBox="0 0 12 12" aria-hidden="true"><circle cx="6" cy="6" r="6" fill="#fff"/><rect x="3" y="4" width="6" height="4" fill="none" stroke="#1b1b1d" stroke-width="1"/><path d="M3 4l3 2.2L9 4" fill="none" stroke="#1b1b1d" stroke-width="1"/></svg>
        marcuspellowcreative@fernmail.example
      </li>
      <li>
        <svg viewBox="0 0 12 12" aria-hidden="true"><circle cx="6" cy="6" r="5.4" fill="none" stroke="#fff" stroke-width="1.2"/><ellipse cx="6" cy="6" rx="2.3" ry="5.4" fill="none" stroke="#fff" stroke-width="1"/><path d="M0.6 6h10.8M1.5 3.5h9M1.5 8.5h9" stroke="#fff" stroke-width="0.9"/></svg>
        www.pellowcreative.example
      </li>
    </ul>
    <p class="abn">ABN 37 512 640 915</p>
  </footer>
</main>
</body>
</html>
```